Business cards & stationery for a cloth diaper retailer
Natural & Organic Baby Products
Bright & Fun-filled
Marisol Treveck
Carvale, MD 20843
info@dotsnugnest.com
www.dotsnugnest.com
My business is web-based so the website address needs to be highlighted on the card.
Services include:
- Cloth diapering workshops
- Newborn rental cloth diaper trial package
- Private In-Home Consults
- Office/Showroom hours

```html
<!DOCTYPE html>
<html lang="en">
<head>
<meta charset="utf-8">
<title>Dot's Snug Nest — Stationery Set</title>
<link href="https://fonts.googleapis.com/css2?family=Open+Sans:wght@400;700&display=swap" rel="stylesheet">
<style>
  :root {
    --page: #ffffff;
    --paper: #ffffff;
    --frame: #e4e4e4;
    --leaf: #7cc242;
    --leaf-deep: #4f9a2a;
    --ink: #555555;
    --shadow: rgba(0,0,0,0.22);
  }
  * { box-sizing: border-box; margin: 0; padding: 0; }
  html, body { width: 1200px; height: 681px; overflow: hidden; background: var(--page); }
  body { font-family: "Open Sans", Arial, sans-serif; color: var(--ink); }
  .canvas { position: relative; width: 1200px; height: 681px; border: 2px solid var(--frame); }
  .sheet { position: absolute; background: var(--paper); box-shadow: 3px 4px 8px var(--shadow); overflow: hidden; }

  .brand { display: flex; align-items: center; gap: 6px; }
  .brand-dot { width: 22px; height: 22px; border-radius: 50%; background: var(--leaf); flex: none; }
  .brand-name { font-weight: 700; color: var(--leaf-deep); font-size: 15px; line-height: 1; white-space: nowrap; }

  .contact { font-size: 6.5px; line-height: 1.45; color: var(--ink); }
  .band { position: absolute; left: 0; right: 0; bottom: 0; background: var(--leaf); }
  .flower { position: absolute; background: radial-gradient(circle at 70% 25%, #6cc13a 0 28%, rgba(124,194,66,0.35) 45%, rgba(255,255,255,0) 70%); }

  /* envelope front */
  .envelope-front { left: 60px; top: 101px; width: 480px; height: 211px; }
  .envelope-front .brand { position: absolute; left: 16px; top: 18px; }
  .envelope-front .contact { position: absolute; left: 16px; top: 72px; }
  .envelope-front .band { height: 10px; }
  .envelope-front .flower { left: 380px; top: 92px; width: 96px; height: 108px; }

  /* envelope back */
  .envelope-back { left: 60px; top: 336px; width: 480px; height: 211px; }
  .envelope-back svg.flap { position: absolute; inset: 0; }
  .envelope-back .brand { position: absolute; left: 50%; top: 60px; transform: translateX(-50%); }
  .envelope-back .brand-name { font-size: 12px; }
  .envelope-back .brand-dot { width: 18px; height: 18px; }

  /* letterhead */
  .letterhead { left: 624px; top: 48px; width: 312px; height: 581px; }
  .letterhead .brand { position: absolute; left: 14px; top: 26px; }
  .letterhead .contact { position: absolute; left: 14px; top: 80px; font-size: 6px; }
  .letterhead .band { height: 12px; }
  .letterhead .flower { left: 212px; top: 440px; width: 94px; height: 126px; }

  /* business cards */
  .card { width: 185px; height: 106px; left: 967px; }
  .card-front { top: 132px; }
  .card-front .brand { position: absolute; left: 8px; top: 10px; }
  .card-front .brand-name { font-size: 10px; }
  .card-front .brand-dot { width: 14px; height: 14px; }
  .card-front .contact { position: absolute; left: 8px; top: 38px; font-size: 5px; }
  .card-front .web { position: absolute; left: 8px; top: 72px; font-size: 5.5px; font-weight: 700; color: var(--leaf-deep); }
  .card-front .band { height: 5px; }
  .card-front .flower { left: 140px; top: 22px; width: 42px; height: 70px; }

  .card-back { top: 259px; text-align: center; }
  .card-back .brand { justify-content: center; margin-top: 14px; }
  .card-back .brand-name { font-size: 9px; }
  .card-back .brand-dot { width: 12px; height: 12px; }
  .card-back .contact { margin-top: 12px; font-size: 5px; }
  .card-back .name { font-weight: 700; }
</style>
</head>
<body>
<main class="canvas">

  <section class="sheet envelope-front" aria-label="Envelope front">
    <div class="brand"><span class="brand-dot"></span><span class="brand-name">Dot's Snug Nest</span></div>
    <div class="contact">
      Carvale, MD 20843<br>
      Toll free: (888) 555-0146<br>
      Fax: (410) 555-0182<br>
      E-mail: info@dotsnugnest.com<br>
      www.dotsnugnest.com
    </div>
    <div class="flower" role="img" aria-label="Green flower on a curving stem"></div>
    <div class="band"></div>
  </section>

  <section class="sheet envelope-back" aria-label="Envelope back">
    <svg class="flap" width="480" height="211" viewBox="0 0 480 211">
      <polyline points="6,6 200,96 280,96 474,6" fill="none" stroke="#9a9a9a" stroke-width="1.2"/>
      <polyline points="0,211 200,96 M280,96 480,211" fill="none" stroke="#d0d0d0" stroke-width="1"/>
    </svg>
    <div class="brand"><span class="brand-dot"></span><span class="brand-name">Dot's Snug Nest</span></div>
  </section>

  <section class="sheet letterhead" aria-label="Letterhead">
    <div class="brand"><span class="brand-dot"></span><span class="brand-name">Dot's Snug Nest</span></div>
    <div class="contact">
      Carvale, MD 20843<br>
      Toll free: (888) 555-0146<br>
      Fax: (410) 555-0182<br>
      E-mail: info@dotsnugnest.com<br>
      www.dotsnugnest.com
    </div>
    <div class="flower" role="img" aria-label="Green flower on a curving stem"></div>
    <div class="band"></div>
  </section>

  <section class="sheet card card-front" aria-label="Business card front">
    <div class="brand"><span class="brand-dot"></span><span class="brand-name">Dot's Snug Nest</span></div>
    <div class="contact">
      <span class="name">Marisol Treveck</span><br>
      Carvale, MD 20843<br>
      (888) 555-0146<br>
      info@dotsnugnest.com<br>
      Skype: marisoltrev
    </div>
    <div class="web">www.dotsnugnest.com</div>
    <div class="flower" role="img" aria-label="Green flower on a curving stem"></div>
    <div class="band"></div>
  </section>

  <section class="sheet card card-back" aria-label="Business card back">
    <div class="brand"><span class="brand-dot"></span><span class="brand-name">Dot's Snug Nest</span></div>
    <div class="contact">
      <span class="name">Marisol Treveck</span><br>
      Cloth Diaper Consultant<br>
      Workshops, Rentals &amp; In-Home Consults<br>
      www.dotsnugnest.com
    </div>
  </section>

</main>
</body>
</html>
```